The name of my company is Tolmen Refacing LLC and I would like the sub text to say "Cabinet Refacing and Countertops". Have my name Dorian Tolmen, Owner / Sales, contact info: Cell: 360-555-0147 / Email: dorian.tolmen@quenmail.com

Simple, Clean, and Organized. With colors that will appeal to the eye.

Target Market(s)

Houses and Apartments

Industry/Entity Type

Cabinet Refacing

Contact Information for Business Card

Company name and sub text Dorian Tolmen - Owner / Sales, my cell phone number and email

Requirements
Must have
• Business name, my name / position, and my contact info
Nice to have
• Simple. Organized. Appealing to the eye

```html
<!DOCTYPE html>
<html lang="en">
<head>
<meta charset="utf-8">
<title>Tolmen Refacing LLC – Business Card</title>
<link rel="stylesheet" href="https://fonts.googleapis.com/css2?family=Montserrat:wght@400;600;700&display=swap">
<style>
  :root {
    --stage: #e4e7ec;
    --paper: #ffffff;
    --ink: #1a1a1a;
    --ink-soft: #3a3a3a;
    --night: #0c0c0c;
    --night-text: #f2f2f2;
    --shadow: rgba(20, 30, 50, 0.22);
  }
  * { box-sizing: border-box; margin: 0; padding: 0; }
  html, body {
    width: 1200px;
    height: 675px;
    overflow: hidden;
    background: var(--stage);
    font-family: "Montserrat", sans-serif;
  }
  .canvas {
    width: 1200px;
    height: 675px;
    display: flex;
    align-items: center;
    justify-content: center;
    gap: 60px;
  }
  .card {
    position: relative;
    width: 510px;
    height: 291px;
    box-shadow: 0 14px 34px var(--shadow);
    overflow: hidden;
  }

  /* Front side */
  .card--front { background: var(--paper); color: var(--ink); }
  .card--front .company {
    position: absolute;
    top: 52px;
    left: 0;
    right: 0;
    text-align: center;
    font-size: 30px;
    font-weight: 600;
    letter-spacing: 2px;
  }
  .card--front .company-suffix {
    position: absolute;
    top: 92px;
    right: 96px;
    font-size: 11px;
    font-weight: 600;
    letter-spacing: 3px;
    color: var(--ink);
  }
  .person {
    position: absolute;
    left: 44px;
    top: 168px;
  }
  .person-name {
    font-size: 21px;
    font-weight: 700;
    letter-spacing: 1px;
  }
  .person-role {
    font-size: 8.5px;
    font-weight: 400;
    letter-spacing: 1px;
    text-align: right;
    margin-top: 2px;
    color: var(--ink-soft);
  }
  .contact {
    position: absolute;
    right: 36px;
    top: 134px;
    list-style: none;
    font-size: 12px;
    color: var(--ink-soft);
  }
  .contact li {
    display: flex;
    align-items: center;
    gap: 7px;
    margin-bottom: 6px;
  }
  .contact svg { width: 11px; height: 11px; fill: var(--ink); flex: none; }
  .tagline-band {
    position: absolute;
    left: 0;
    right: 0;
    bottom: 30px;
    height: 30px;
    background: var(--night);
    color: var(--night-text);
    display: flex;
    align-items: center;
    justify-content: center;
    font-size: 12.5px;
    font-weight: 700;
    letter-spacing: 2px;
  }

  /* Back side */
  .card--back {
    background: var(--night);
    color: var(--night-text);
    display: flex;
    flex-direction: column;
    align-items: center;
    justify-content: center;
  }
  .card--back .company {
    font-size: 32px;
    font-weight: 600;
    letter-spacing: 2px;
  }
  .card--back .company-suffix {
    align-self: flex-end;
    margin-right: 70px;
    font-size: 11px;
    font-weight: 600;
    letter-spacing: 3px;
  }
  .card--back .tagline {
    margin-top: 22px;
    font-size: 13px;
    font-weight: 700;
    letter-spacing: 2px;
  }
</style>
</head>
<body>
<main class="canvas">
  <section class="card card--front" aria-label="Business card front">
    <h1 class="company">TOLMEN REFACING</h1>
    <span class="company-suffix">LLC</span>
    <div class="person">
      <p class="person-name">DORIAN TOLMEN</p>
      <p class="person-role">OWNER / SALES</p>
    </div>
    <ul class="contact">
      <li>
        <svg viewBox="0 0 24 24" aria-hidden="true"><path d="M6.6 10.8a15.1 15.1 0 0 0 6.6 6.6l2.2-2.2c.3-.3.7-.4 1-.2 1.1.4 2.3.6 3.6.6.6 0 1 .4 1 1V20c0 .6-.4 1-1 1C10.6 21 3 13.4 3 4c0-.6.4-1 1-1h3.5c.6 0 1 .4 1 1 0 1.3.2 2.5.6 3.6.1.3 0 .7-.2 1z"/></svg>
        360-555-0147
      </li>
      <li>
        <svg viewBox="0 0 24 24" aria-hidden="true"><path d="M2 5h20v14H2zm2 2v.5l8 5 8-5V7zm0 2.8V17h16V9.8l-8 5z"/></svg>
        dorian.tolmen@quenmail.com
      </li>
    </ul>
    <div class="tagline-band">CABINET REFACING &amp; COUNTERTOPS</div>
  </section>

  <section class="card card--back" aria-label="Business card back">
    <h2 class="company">TOLMEN REFACING</h2>
    <span class="company-suffix">LLC</span>
    <p class="tagline">CABINET REFACING &amp; COUNTERTOPS</p>
  </section>
</main>
</body>
</html>
```